" Empresa nova no mercado, clínica ainda em fase de acabamento, pretendo oferecer consultas e exames a preços acessíveis, em ambiente confortável, seguro e acolhedor, com o compromisso de oferecer o melhor atendimento a cada paciente. "

```html
<!DOCTYPE html>
<html lang="pt-BR">
<head>
<meta charset="UTF-8">
<title>VitaClínica – Papelaria</title>
<link href="https://fonts.googleapis.com/css2?family=Montserrat:wght@400;600;700&display=swap" rel="stylesheet">
<style>
  :root {
    --teal: #4aa8ae;
    --teal-dark: #3a949a;
    --teal-soft: #6dbcc1;
    --paper: #ffffff;
    --backdrop: #e9ebea;
    --ink-muted: #7f9a9c;
  }
  * { box-sizing: border-box; margin: 0; padding: 0; }
  html, body { width: 1200px; height: 1200px; overflow: hidden; }
  body {
    background: var(--backdrop);
    font-family: "Montserrat", Arial, sans-serif;
    position: relative;
  }

  /* Business card */
  .business-card {
    position: absolute;
    left: 70px; top: 300px;
    width: 330px; height: 600px;
    background: var(--teal);
    overflow: hidden;
    box-shadow: 0 6px 18px rgba(0,0,0,.12);
  }
  .business-card .brand {
    position: absolute;
    left: 165px; top: 40px;
    transform-origin: left top;
    transform: rotate(90deg) translateX(0) translateY(-60px);
    display: flex; align-items: center; gap: 12px;
    white-space: nowrap;
    color: var(--paper);
  }
  .brand-dot {
    width: 30px; height: 30px; border-radius: 50%;
    background: currentColor;
  }
  .brand-name { font-weight: 700; font-size: 30px; letter-spacing: .5px; }
  .brand-tagline {
    font-size: 9px; font-weight: 400; letter-spacing: 1.5px;
    text-transform: uppercase; margin-top: 2px;
  }
  .business-card .faint-disc {
    position: absolute;
    left: 120px; top: 350px;
    width: 300px; height: 300px; border-radius: 50%;
    background: rgba(255,255,255,.09);
  }

  /* Envelope */
  .envelope {
    position: absolute;
    left: 450px; top: 420px;
    width: 700px; height: 350px;
    background: var(--paper);
    box-shadow: 0 6px 18px rgba(0,0,0,.12);
    overflow: hidden;
  }
  .envelope-flap { position: absolute; inset: 0; }
  .envelope .brand {
    position: absolute;
    left: 170px; top: 140px;
    display: flex; align-items: center; gap: 14px;
    color: var(--teal);
  }
  .envelope .brand-dot { width: 40px; height: 40px; }
  .envelope .brand-name { font-size: 40px; }
  .envelope .brand-tagline { color: var(--ink-muted); font-size: 9px; }

  .contact-list {
    position: absolute;
    left: 420px; top: 215px;
    list-style: none;
    font-size: 10px; color: var(--ink-muted);
  }
  .contact-list li {
    display: flex; align-items: center; gap: 8px;
    height: 20px;
  }
  .contact-icon { width: 12px; height: 12px; flex: none; }
</style>
</head>
<body>

  <section class="business-card" aria-label="Cartão de visita">
    <div class="faint-disc"></div>
    <div class="brand">
      <span class="brand-dot"></span>
      <div>
        <div class="brand-name">VitaClínica</div>
        <div class="brand-tagline">Consultas e exames com acolhimento</div>
      </div>
    </div>
  </section>

  <section class="envelope" aria-label="Envelope">
    <svg class="envelope-flap" width="700" height="350" viewBox="0 0 700 350">
      <rect x="0" y="0" width="700" height="10" fill="var(--teal)"/>
      <path d="M600 0 L700 0 L700 350 L600 350 Q586 350 590 334 L640 200 Q646 175 640 150 L590 16 Q586 0 600 0 Z" fill="var(--teal)"/>
      <circle cx="70" cy="200" r="160" fill="var(--teal)" opacity=".05"/>
    </svg>

    <div class="brand">
      <span class="brand-dot"></span>
      <div>
        <div class="brand-name">VitaClínica</div>
        <div class="brand-tagline">Consultas e exames com acolhimento</div>
      </div>
    </div>

    <ul class="contact-list">
      <li>
        <svg class="contact-icon" viewBox="0 0 12 12"><rect x="1" y="2.5" width="10" height="7" rx="1" fill="none" stroke="var(--teal)" stroke-width="1.2"/><path d="M1.5 3 L6 6.5 L10.5 3" fill="none" stroke="var(--teal)" stroke-width="1.2"/></svg>
        contato@vitaclinica.com.br
      </li>
      <li>
        <svg class="contact-icon" viewBox="0 0 12 12"><path d="M3 1 L5 3.5 L4 5 Q5 7 7 8 L8.5 7 L11 9 L9.5 11 Q4 10.5 1 3 Z" fill="var(--teal)"/></svg>
        (11) 4002-1234
      </li>
      <li>
        <svg class="contact-icon" viewBox="0 0 12 12"><rect x="3" y="0.8" width="6" height="10.4" rx="1.2" fill="none" stroke="var(--teal)" stroke-width="1.2"/><circle cx="6" cy="9.2" r=".8" fill="var(--teal)"/></svg>
        (11) 98765-4321
      </li>
      <li>
        <svg class="contact-icon" viewBox="0 0 12 12"><path d="M6 11.5 Q1.5 6.5 1.5 4.5 A4.5 4.5 0 0 1 10.5 4.5 Q10.5 6.5 6 11.5 Z" fill="var(--teal)"/><circle cx="6" cy="4.5" r="1.6" fill="#fff"/></svg>
        Rua das Acácias, 250
      </li>
    </ul>
  </section>

</body>
</html>
```